Brownie Snack Packaging

Design the film wrapper packaging for a brownie snack. It needs to be cohesive with our existing product line (please review attached photos), but still differentiated from it to avoid customer confusion.
Brief is outlined in the images attached. Please review prior to submitting designs. All designs should have the iridescent white pearl packaging color, with the text:
High Protein Brownie
10g Protein
Vegan
Gluten-Free
No Added Sugars
We would like to see designs with square packaging with a mouth-watering brownie image being the most prominent. Logo of brand "ORUNE" should be in upper right corner.
Note: we have another product line of cashew butter sachets that are pink, blue, & chocolate - I'm attaching those for reference so you can design these brownies to look somewhat related to the cashew butters.
Look and feel
Each slider illustrates characteristics of the customer's brand and the style your logo design should communicate.

```html
<!DOCTYPE html>
<html lang="en">
<head>
<meta charset="utf-8">
<title>ORUNE High Protein Brownie – Wrapper Front</title>
<link href="https://fonts.googleapis.com/css2?family=Jost:wght@400&family=Playfair+Display:wght@800;900&family=Quicksand:wght@500;600&display=swap" rel="stylesheet">
<style>
  :root {
    --backdrop: #e4e4e3;
    --pearl: #ffffff;
    --cocoa: #55301c;
    --cream: #f5e4c9;
    --gold: #b8892c;
    --ink: #141414;
    --label-text: #f3e6d4;
  }
  * { box-sizing: border-box; margin: 0; padding: 0; }
  html, body {
    width: 1200px;
    height: 900px;
    overflow: hidden;
    background: var(--backdrop);
  }
  .canvas {
    position: relative;
    width: 1200px;
    height: 900px;
  }
  .wrapper-front {
    position: absolute;
    left: 256px;
    top: 60px;
    width: 689px;
    height: 781px;
    background: var(--pearl);
  }
  .protein-tab {
    position: absolute;
    left: 524px;
    top: 0;
    width: 103px;
    height: 164px;
    background: var(--cocoa);
    border-radius: 0 0 6px 6px;
    color: var(--pearl);
    font-family: "Quicksand", sans-serif;
    text-align: center;
    padding-top: 68px;
  }
  .protein-tab .amount {
    display: block;
    font-size: 40px;
    font-weight: 600;
    line-height: 1;
  }
  .protein-tab .unit {
    display: block;
    font-size: 18px;
    font-weight: 600;
    letter-spacing: 0.5px;
    margin-top: 4px;
  }
  .brand-name {
    position: absolute;
    left: 66px;
    top: 58px;
    font-family: "Jost", sans-serif;
    font-weight: 400;
    font-size: 124px;
    line-height: 1;
    letter-spacing: 2px;
    color: var(--gold);
  }
  .product-panel {
    position: absolute;
    left: 31px;
    top: 417px;
    width: 626px;
    height: 183px;
    background: var(--cream);
    border-radius: 10px;
  }
  .product-photo {
    position: absolute;
    left: 156px;
    top: 178px;
    width: 372px;
    height: 296px;
    border-radius: 14px 24px 10px 10px;
    background: linear-gradient(160deg, #7a3f22 0%, #5b2b16 45%, #3d1a0c 100%);
  }
  .product-title {
    position: absolute;
    left: 31px;
    top: 480px;
    width: 626px;
    text-align: center;
    font-family: "Playfair Display", serif;
    color: var(--ink);
    line-height: 1;
  }
  .product-title .line-small {
    display: block;
    font-size: 42px;
    font-weight: 800;
    letter-spacing: 1.5px;
  }
  .product-title .line-large {
    display: block;
    font-size: 66px;
    font-weight: 900;
    letter-spacing: 1px;
    margin-top: 2px;
  }
  .claims-bar {
    position: absolute;
    left: 31px;
    top: 610px;
    width: 626px;
    height: 90px;
    background: var(--cocoa);
    border-radius: 8px;
    display: flex;
    align-items: center;
  }
  .claim {
    flex: 1;
    text-align: center;
    font-family: "Quicksand", sans-serif;
    font-weight: 500;
    font-size: 22px;
    line-height: 1;
    letter-spacing: 1px;
    color: var(--label-text);
  }
  .claim-divider {
    width: 2px;
    height: 66px;
    background: var(--label-text);
  }
</style>
</head>
<body>
  <main class="canvas">
    <section class="wrapper-front">
      <div class="protein-tab">
        <span class="amount">10g</span>
        <span class="unit">protein</span>
      </div>

      <div class="brand-name">ORUNE</div>

      <div class="product-panel"></div>
      <div class="product-photo" role="img" aria-label="Photo of three stacked chocolate brownies drizzled with melted chocolate"></div>

      <h1 class="product-title">
        <span class="line-small">HIGH PROTEIN</span>
        <span class="line-large">BROWNIE</span>
      </h1>

      <div class="claims-bar">
        <p class="claim">no added<br>sugars</p>
        <span class="claim-divider"></span>
        <p class="claim">vegan</p>
        <span class="claim-divider"></span>
        <p class="claim">gluten<br>free</p>
      </div>
    </section>
  </main>
</body>
</html>
```